Lumo Vessa Wigs " Styling Foam"

I need a label created for my product . The bottle size is 50ml so it must be designed to fit that size bottle. I will post my logo and examples of my bottle size. I want the label design to be simple and cute. ill also add pictures of my website, so you can get ideas from there. The bottle is white so I want the main colors to be white and pink. All colors on the label must match my logo. I love glitter as well.

I know for sure I want my logo big, and I want "Styling Foam'',
then under styling foam I would like " Medium Hold" in a different front. be very creative.

Then under that I would like it to say " No Alcohol , Saulfate or Paraben

please make sure on the label in the front it has "NET: 7.0 oz / 200g" so people know what size it is.

I would like a glitter border on the label.

I also want the back of the label to have directions.

And ingredients list too . Very small not too big at all.

Target Market(s)

My target market is woman of all ages .. but mainly woman from ages 26-65

Industry/Entity Type

Hair And Beauty

Font styles to use
Serif
Sans Serif
Decorative
Script

Colors
e667a6
eda3c7
f9d9e8
e34297

Requirements
Must have
• The project must match the colors of my logo, it must have a nice pretty glitter border . It must be simple and clean . But still stylish ! I don’t want everything after my logo to be in the same font . Have fun with this design, be creative. My logo and “ Styling Foam” must be the two centerpiece!
Nice to have
• It will be nice to have different fonts! And nice to have all the colors that match my logo
Must be expensive looking !!
Very eye catching!
Should not have
• Do not add colors that my logo doesn’t have !!!!
I don’t want it to look too plain and boring ! I want it to be classy and expensive looking !

```html
<!DOCTYPE html>
<html lang="en">
<head>
<meta charset="utf-8">
<title>Lumo Vessa Wigs – Styling Foam Labels</title>
<link href="https://fonts.googleapis.com/css2?family=Abril+Fatface&family=Oswald:wght@300;400&family=Roboto+Condensed:wght@700&family=Roboto:wght@700&display=swap" rel="stylesheet">
<style>
  :root {
    --pink-deep: #e34297;
    --pink: #e667a6;
    --pink-soft: #eda3c7;
    --pink-pale: #f9d9e8;
    --ink: #231f20;
    --grey-text: #6d6e70;
    --white: #ffffff;
    --frame: #8a8a8a;
    --cap-edge: #b3b3b3;
    --cap-mid: #d2d3d3;
    --cap-face: #e3e5e5;
    --label-edge: #b9b9b9;
  }
  * { margin: 0; padding: 0; box-sizing: border-box; }
  html, body { width: 1200px; height: 891px; overflow: hidden; background: var(--white); }
  .canvas {
    position: relative; width: 1200px; height: 891px;
    border: 1px solid var(--frame); background: var(--white);
    font-family: "Roboto", Arial, sans-serif;
  }
  .bottle { position: absolute; top: 46px; width: 226px; height: 800px; }
  .bottle--side { left: 330px; }
  .bottle--front { left: 644px; }
  .cap {
    position: absolute; left: 0; top: 0; width: 226px; height: 273px;
    border: 1px solid var(--cap-edge);
    background: linear-gradient(90deg,
      var(--cap-mid) 0 12%, #dadbdb 12% 25%, var(--cap-face) 25% 74%,
      #d6d7d7 74% 88%, var(--cap-edge) 88% 100%);
  }
  .label {
    position: absolute; left: 0; top: 273px; width: 226px; height: 527px;
    background: var(--white); border: 1px solid var(--label-edge); overflow: hidden;
  }
  .label--textured { background: linear-gradient(160deg, #fbfbfb, #f1f1f1 60%, #f8f8f8); }
  .glitter { position: absolute; left: 0; width: 100%; }
  .glitter--top {
    top: 0; height: 52px;
    background: linear-gradient(180deg, var(--pink-deep) 0%, var(--pink) 35%, var(--pink-soft) 70%, rgba(249,217,232,0) 100%);
  }
  .glitter--bottom {
    bottom: 0; height: 46px;
    background: linear-gradient(0deg, var(--pink-deep) 0%, var(--pink) 35%, var(--pink-soft) 70%, rgba(249,217,232,0) 100%);
  }
  .brand {
    position: absolute; font-family: "Oswald", Arial, sans-serif; font-weight: 400;
    color: var(--pink-deep); text-align: center; text-transform: uppercase; line-height: 1.05;
  }
  .brand--side { left: 18px; top: 193px; width: 110px; font-size: 19px; letter-spacing: 1px; }
  .brand--front { left: 20px; top: 40px; width: 186px; font-size: 30px; letter-spacing: 2px; }
  .hold-light {
    position: absolute; left: 20px; top: 274px;
    font-family: "Oswald", Arial, sans-serif; font-weight: 300;
    font-size: 31px; line-height: 1.08; color: var(--ink); text-transform: uppercase;
  }
  .product-vertical {
    position: absolute; left: 141px; top: 478px;
    transform: rotate(-90deg); transform-origin: 0 0;
    font-family: "Abril Fatface", Georgia, serif; font-size: 60px;
    color: var(--pink-deep); white-space: nowrap; line-height: 1;
  }
  .accent-disc { position: absolute; left: 76px; top: 158px; width: 70px; height: 70px; border-radius: 50%; background: radial-gradient(circle at 40% 40%, var(--pink), var(--pink-deep)); }
  .product-title {
    position: absolute; left: 0; top: 245px; width: 226px; text-align: center;
    font-family: "Abril Fatface", Georgia, serif; font-size: 46px; line-height: 0.78; color: var(--ink);
  }
  .hold-badge { position: absolute; left: 66px; top: 349px; width: 90px; height: 48px; }
  .hold-badge__text {
    position: absolute; inset: 0; display: flex; flex-direction: column; align-items: center; justify-content: center;
    font-family: "Roboto Condensed", Arial, sans-serif; font-weight: 700; text-transform: uppercase; line-height: 0.95;
  }
  .hold-badge__top { font-size: 15px; color: var(--grey-text); }
  .hold-badge__main { font-size: 24px; color: var(--pink-deep); }
  .free-from { position: absolute; display: flex; gap: 5px; }
  .free-from--side { left: 20px; top: 446px; }
  .free-from--front { left: 84px; top: 424px; }
  .net {
    position: absolute; font-family: "Roboto", Arial, sans-serif; font-weight: 700;
    font-size: 10.5px; color: var(--ink); white-space: nowrap;
  }
  .net--side { left: 20px; top: 468px; }
  .net--front { left: 0; width: 226px; text-align: center; top: 460px; }
</style>
</head>
<body>
<div class="canvas">

  <section class="bottle bottle--side" aria-label="Styling foam bottle, side label">
    <div class="cap"></div>
    <div class="label label--textured">
      <div class="glitter glitter--top" role="img" aria-label="Pink glitter border"></div>
      <div class="brand brand--side">Lumo Vessa<br>Wigs</div>
      <div class="hold-light">Medium<br>Hold</div>
      <div class="product-vertical">Styling Foam</div>
      <div class="free-from free-from--side" aria-label="Free from alcohol, sulfate and paraben">
        <svg width="18" height="18" viewBox="0 0 18 18"><circle cx="9" cy="9" r="8" fill="none" stroke="#231f20" stroke-width="1"/><path d="M4 14 14 4" stroke="#231f20" stroke-width="1"/><rect x="7" y="6" width="4" height="7" fill="none" stroke="#231f20" stroke-width="0.8"/></svg>
        <svg width="18" height="18" viewBox="0 0 18 18"><circle cx="9" cy="9" r="8" fill="none" stroke="#231f20" stroke-width="1"/><path d="M4 14 14 4" stroke="#231f20" stroke-width="1"/><path d="M9 5 12 12H6Z" fill="none" stroke="#231f20" stroke-width="0.8"/></svg>
      </div>
      <div class="net net--side">NET: 7.0 oz / 200g</div>
      <div class="glitter glitter--bottom" role="img" aria-label="Pink glitter border"></div>
    </div>
  </section>

  <section class="bottle bottle--front" aria-label="Styling foam bottle, front label">
    <div class="cap"></div>
    <div class="label">
      <div class="brand brand--front">Lumo Vessa<br>Wigs</div>
      <div class="accent-disc" role="img" aria-label="Pink disc with contour-line texture"></div>
      <div class="product-title">styling<br>foam</div>
      <div class="hold-badge">
        <svg width="90" height="48" viewBox="0 0 90 48" aria-hidden="true">
          <path d="M9 1H1V47H9M81 1H89V47H81" fill="none" stroke="#e34297" stroke-width="2"/>
        </svg>
        <div class="hold-badge__text"><span class="hold-badge__top">Medium</span><span class="hold-badge__main">Hold</span></div>
      </div>
      <div class="free-from free-from--front" aria-label="Free from alcohol, sulfate and paraben">
        <svg width="22" height="22" viewBox="0 0 18 18"><circle cx="9" cy="9" r="8" fill="none" stroke="#231f20" stroke-width="1"/><path d="M4 14 14 4" stroke="#231f20" stroke-width="1"/><rect x="7" y="6" width="4" height="7" fill="none" stroke="#231f20" stroke-width="0.8"/></svg>
        <svg width="22" height="22" viewBox="0 0 18 18"><circle cx="9" cy="9" r="8" fill="none" stroke="#231f20" stroke-width="1"/><path d="M4 14 14 4" stroke="#231f20" stroke-width="1"/><path d="M9 5 12 12H6Z" fill="none" stroke="#231f20" stroke-width="0.8"/></svg>
      </div>
      <div class="net net--front">NET: 7.0 oz / 200g</div>
      <div class="glitter glitter--bottom" role="img" aria-label="Pink glitter border"></div>
    </div>
  </section>

</div>
</body>
</html>
```